Aged Care Consultancy Business needs a business card design

I need a two sided business card - I want it clean and professional. Surprise me

Target Market(s)

middle aged and ageing victorians

Industry/Entity Type

Health Care

Contact Information for Business Card

Text to be included

Logo
Aged Care Consulting Services
Professional, Reliable, Affordable

Orin Tessaldo
Director
0472 31 64 09 (larger)
1300 31 64 09
orin@valtrino.com.au
www.valtrinocare.com.au
Facebook (details TBA)

include little icons beside the contact info:

- Envelope = email
- Phone = phone
- Globe = website

Font styles to use
Serif
Sans Serif

Requirements
Must have
• look proffesional and clean

```html
<!DOCTYPE html>
<html lang="en">
<head>
<meta charset="utf-8">
<title>Valtrino Care Business Card</title>
<link rel="stylesheet" href="https://fonts.googleapis.com/css2?family=Open+Sans:wght@400;600;700&display=swap">
<style>
  :root {
    --navy: #1d4584;
    --ink: #222630;
    --paper: #ffffff;
    --stage: #e9e6e1;
    --card-blue: #1e4a8a;
  }
  * { margin: 0; padding: 0; box-sizing: border-box; }
  html, body {
    width: 1200px; height: 1000px; overflow: hidden;
    background: var(--stage);
    font-family: "Open Sans", Arial, sans-serif;
  }
  .canvas { position: relative; width: 1200px; height: 1000px; }
  .card {
    position: absolute; left: 265px; width: 665px; height: 397px;
    border-radius: 24px; overflow: hidden;
    box-shadow: 0 2px 6px rgba(0,0,0,0.15);
  }
  .card-front { top: 73px; background: var(--paper); }
  .card-back { top: 532px; background: var(--card-blue); }

  .brand-name {
    position: absolute; left: 32px; top: 140px;
    font-size: 46px; font-weight: 700; color: var(--navy);
    letter-spacing: -0.5px; line-height: 1;
  }

  .contact-list { position: absolute; left: 32px; top: 262px; list-style: none; }
  .contact-item {
    display: flex; align-items: center; gap: 6px;
    font-size: 16px; color: var(--ink); height: 24px;
  }
  .contact-item.primary { font-size: 22px; height: 34px; margin-bottom: 6px; }
  .contact-item svg { width: 16px; height: 16px; fill: var(--navy); flex: none; }
  .contact-item.primary svg { width: 20px; height: 20px; }

  .person { position: absolute; right: 32px; top: 206px; text-align: right; }
  .person-name { font-size: 22px; font-weight: 700; color: var(--navy); letter-spacing: 0.3px; line-height: 1.2; }
  .person-role { font-size: 15px; color: var(--ink); }

  .social {
    position: absolute; right: 32px; top: 320px;
    display: flex; align-items: center; gap: 7px;
    font-size: 16px; color: var(--ink);
  }
  .social-square { width: 12px; height: 14px; background: var(--navy); }
  .service-line { position: absolute; right: 32px; top: 348px; font-size: 16px; color: var(--ink); }

  .back-brand {
    position: absolute; left: 0; right: 0; top: 150px; text-align: center;
    font-size: 62px; font-weight: 700; color: var(--paper); line-height: 1;
  }
  .tagline {
    position: absolute; left: 0; right: 0; top: 348px; text-align: center;
    font-size: 16px; color: var(--paper);
  }
</style>
</head>
<body>
<div class="canvas">
  <section class="card card-front">
    <div class="brand-name">valtrino care</div>

    <ul class="contact-list">
      <li class="contact-item primary">
        <svg viewBox="0 0 24 24" aria-hidden="true"><path d="M6.6 10.8a15.1 15.1 0 0 0 6.6 6.6l2.2-2.2a1 1 0 0 1 1-.25 11.4 11.4 0 0 0 3.6.57 1 1 0 0 1 1 1V20a1 1 0 0 1-1 1A17 17 0 0 1 3 4a1 1 0 0 1 1-1h3.5a1 1 0 0 1 1 1c0 1.25.2 2.45.57 3.57a1 1 0 0 1-.25 1z"/></svg>
        0472 31 64 09
      </li>
      <li class="contact-item">
        <svg viewBox="0 0 24 24" aria-hidden="true"><path d="M3 8c3-4 15-4 18 0l-3 3-3-2V7H9v2l-3 2zM5 13l3-2h8l3 2v7H5z"/></svg>
        1300 31 64 09
      </li>
      <li class="contact-item">
        <svg viewBox="0 0 24 24" aria-hidden="true"><path d="M2 5h20v14H2zm2 2v.5l8 5.5 8-5.5V7z"/></svg>
        orin@valtrino.com.au
      </li>
      <li class="contact-item">
        <svg viewBox="0 0 24 24" aria-hidden="true"><path d="M12 2a10 10 0 1 0 0 20 10 10 0 0 0 0-20zm6.9 6h-3a15 15 0 0 0-1.3-3.9A8 8 0 0 1 18.9 8zM12 4c.8 1.2 1.5 2.5 1.9 4h-3.8c.4-1.5 1.1-2.8 1.9-4zM4.3 14a8 8 0 0 1 0-4h3.4a16 16 0 0 0 0 4zm.8 2h3a15 15 0 0 0 1.3 3.9A8 8 0 0 1 5.1 16zm3-8h-3a8 8 0 0 1 4.3-3.9A15 15 0 0 0 8.1 8zM12 20c-.8-1.2-1.5-2.5-1.9-4h3.8c-.4 1.5-1.1 2.8-1.9 4zm2.3-6H9.7a14 14 0 0 1 0-4h4.6a14 14 0 0 1 0 4zm.3 5.9a15 15 0 0 0 1.3-3.9h3a8 8 0 0 1-4.3 3.9zM16.3 14a16 16 0 0 0 0-4h3.4a8 8 0 0 1 0 4z"/></svg>
        www.valtrinocare.com.au
      </li>
    </ul>

    <div class="person">
      <div class="person-name">ORIN TESSALDO</div>
      <div class="person-role">Director</div>
    </div>

    <div class="social">/valtrinocarecentre <span class="social-square"></span></div>
    <div class="service-line">Aged Care Consulting Services</div>
  </section>

  <section class="card card-back">
    <div class="back-brand">valtrino care</div>
    <div class="tagline">Professional, Reliable, Affordable</div>
  </section>
</div>
</body>
</html>
```